Natural Essential Oil Packaging

We would like you to develop a line of packaging for natural essential oil products from a company named “Kieu Phong Dat.”
List of items to be designed:
- 01 Company logo
- Air freshener (spray) product: 01 Package design + 01 label design
- 02 essential oil (glass containers) variants: 02 Label designs + 01 “how to use” attached instruction tag
Description:
A. Company logo:
- Company name: Kieu Phong Dat (“Tram” is the Vietnamese name for melaleuca);
- symbolizing "pure, natural, untouched, Kieu Phong Dat, essential,";
- should consist of text and graphic;
- should suggest a stylized drop of oil;
B. Air freshener (spray) product (Packaging and label design)
a. Product description
- Oil extracted from the unique Vietnamese cajeput trees
- Strength: pleasant aroma, air cleansing, virus and bacteria cleaning and prevention, insect expelling
- Used for: air refreshing, relaxing, spa-effect, air cleaning, air-born virus prevention (flu virus), insect expelling
- Application: air spray
b. Package to design: 170ml glass spray bottle
c. Label text for design: brand name: Zovetta + variant name “Lemongrass” + Air Freshener + Melaleuca Essential Oil
C. 02 essential oil (glass containers) variants (Label and Instrution Tag designs)
a. Production description:
i. 02 product variant under the brand name Quirandol
1 - Vietnamese Cajeput Oil: Special breed of cajeput only found in Vietnam, known for amazingly pleasant fragrance giving senses of relaxation, refreshment, peace while at the same time, driving off potential disease carrying elements in the air
2 - Australian tea trea oil: Australian breed of malaleuca known for effective healing of skin from various types of infection, skin protection and highly effective oral hygiene
ii. Product values:
1. 100% pure oil, 100% organic, 100% environment and human friendly, NO chemical
2. aiming to promote human’s well being, health, nature sustainability, improve living environment
3. both products are about nurturing, uplifting, healing and recovering
4. both place their values on authenticity, originality, nature, exotic natural ingredients, green and organic life style
5. both have zero chemical and artificial substance hence 100% safe for long time and frequent usage
iii. SKU: 10ml glass container
iv. Application: for both topical and oral use
b. Label text for design:
i. brand name: Quirandol + variant name: Cajeput Oil / Tea Tree Oil
D. Creative elements are suggested to be communicating organicity, understated premiumness, nature, lightness, nurturing
PLEASE SEE ATTACHED FILES FOR BETTER BRIEF DETAILS AND LAYOUTS.

```html
<!DOCTYPE html>
<html lang="en">
<head>
<meta charset="utf-8">
<title>Kieu Phong Dat – Essential Oil Labels</title>
<link rel="stylesheet" href="https://fonts.googleapis.com/css2?family=Alegreya:wght@400;500&family=Alegreya+Sans:wght@400&display=swap">
<style>
  :root {
    --page: #ffffff;
    --label: #f1e6cb;
    --ink: #4a3b20;
    --ink-soft: #5e4d33;
    --ornament-a: #e4d4b2;
    --ornament-b: #cdb58c;
    --caption: #2a2a2a;
    --mark: #a8786a;
    --wordmark: #141414;
  }
  * { margin: 0; padding: 0; box-sizing: border-box; }
  html, body { width: 1200px; height: 900px; overflow: hidden; background: var(--page); }
  .sheet { position: relative; width: 1200px; height: 900px; }

  .caption {
    position: absolute; width: 291px; text-align: center;
    font-family: "Alegreya", serif; font-size: 12px; letter-spacing: .3px;
    color: var(--caption);
  }

  .label { position: absolute; background: var(--label); color: var(--ink); }
  .label.tall { width: 291px; height: 396px; }
  .label.wide { width: 524px; height: 276px; }

  .line { position: absolute; left: 0; right: 0; text-align: center; }
  .maker { font-family: "Alegreya", serif; font-size: 15px; letter-spacing: 1px; color: var(--ink); }
  .brand { font-family: "Alegreya", serif; font-size: 25px; font-weight: 500; color: var(--ink); }
  .variant { font-family: "Alegreya", serif; font-size: 30px; font-weight: 500; color: var(--ink); z-index: 1; }
  .fine { font-family: "Alegreya Sans", sans-serif; font-size: 6.5px; color: var(--ink-soft); z-index: 1; }
  .subtitle { font-family: "Alegreya", serif; font-size: 12px; color: var(--ink); }
  .copy {
    position: absolute; left: 30px; right: 30px; text-align: center;
    font-family: "Alegreya Sans", sans-serif; font-size: 9.2px; line-height: 14px; color: var(--ink-soft);
  }
  .copy p + p { margin-top: 14px; }

  .ornament {
    position: absolute; left: 50%; transform: translateX(-50%);
    background: linear-gradient(90deg, var(--ornament-a), var(--ornament-b) 50%, var(--ornament-a));
    opacity: .7; border-radius: 3px;
  }

  .wordmark {
    position: absolute; left: 632px; top: 700px; width: 565px; height: 110px;
    display: flex; align-items: center; gap: 18px;
  }
  .wordmark-dot { width: 70px; height: 70px; border-radius: 50%; background: var(--mark); flex: none; }
  .wordmark-name {
    font-family: "Alegreya", serif; font-size: 58px; font-weight: 400;
    letter-spacing: 2px; color: var(--wordmark); white-space: nowrap;
  }
</style>
</head>
<body>
<main class="sheet">

  <div class="caption" style="left:22px;top:10px;">(FRONT PACKAGING)</div>
  <div class="caption" style="left:332px;top:10px;">(BACK PACKAGING)</div>
  <div class="caption" style="left:26px;top:454px;">(FRONT PACKAGING)</div>
  <div class="caption" style="left:336px;top:454px;">(BACK PACKAGING)</div>

  <!-- Cajeput front -->
  <section class="label tall" style="left:22px;top:35px;">
    <div class="line maker" style="top:50px;">KIEU PHONG DAT</div>
    <div class="line brand" style="top:68px;">Quirandol</div>
    <div class="ornament" role="img" aria-label="Ornamental scroll band" style="top:175px;width:222px;height:34px;"></div>
    <div class="line variant" style="top:144px;">Cajeput Oil</div>
    <div class="line fine" style="top:206px;">100% pure oil, 100% organic, 100% environment and human friendly</div>
    <div class="line fine" style="top:215px;">10ml glass container</div>
  </section>

  <!-- Cajeput back -->
  <section class="label tall" style="left:332px;top:35px;">
    <div class="line maker" style="top:20px;">KIEU PHONG DAT</div>
    <div class="line brand" style="top:38px;">Quirandol</div>
    <div class="ornament" role="img" aria-label="Ornamental scroll band" style="top:106px;width:230px;height:32px;"></div>
    <div class="copy" style="top:145px;">
      <p>100% pure oil, 100% organic, 100% environment and human friendly.<br>Topical and oral use.</p>
      <p>Vietnamese Cajeput Oil: Special breed of cajeput only found in Vietnam, known for amazingly pleasant fragrance giving senses of relaxation, refreshment, peace while at the same time, driving off potential disease carrying elements in the air.</p>
    </div>
    <div class="ornament" role="img" aria-label="Ornamental scroll band" style="top:255px;width:230px;height:32px;"></div>
  </section>

  <!-- Tea tree front -->
  <section class="label tall" style="left:26px;top:479px;">
    <div class="line maker" style="top:50px;">KIEU PHONG DAT</div>
    <div class="line brand" style="top:68px;">Quirandol</div>
    <div class="ornament" role="img" aria-label="Ornamental scroll band" style="top:175px;width:222px;height:34px;"></div>
    <div class="line variant" style="top:144px;">Tea Tree Oil</div>
    <div class="line fine" style="top:206px;">100% pure oil, 100% organic, 100% environment and human friendly</div>
    <div class="line fine" style="top:215px;">10ml glass container</div>
  </section>

  <!-- Tea tree back -->
  <section class="label tall" style="left:336px;top:479px;">
    <div class="line maker" style="top:20px;">KIEU PHONG DAT</div>
    <div class="line brand" style="top:38px;">Quirandol</div>
    <div class="ornament" role="img" aria-label="Ornamental scroll band" style="top:106px;width:230px;height:32px;"></div>
    <div class="copy" style="top:145px;">
      <p>100% pure oil, 100% organic, 100% environment and human friendly.<br>Topical and oral use.</p>
      <p>Australian tea trea oil: Australian breed of malaleuca known for effective healing of skin from various types of infection, skin protection and highly effective oral hygiene</p>
    </div>
    <div class="ornament" role="img" aria-label="Ornamental scroll band" style="top:240px;width:230px;height:32px;"></div>
  </section>

  <!-- Air freshener label -->
  <section class="label wide" style="left:658px;top:36px;">
    <div class="line maker" style="top:36px;">KIEU PHONG DAT</div>
    <div class="line brand" style="top:54px;font-size:22px;">Zovetta</div>
    <div class="ornament" role="img" aria-label="Ornamental scroll band" style="top:142px;width:150px;height:34px;"></div>
    <div class="line variant" style="top:112px;font-size:32px;">Lemongrass</div>
    <div class="line subtitle" style="top:180px;">Melaleuca Essential Oil Air Freshener</div>
    <div class="line fine" style="top:197px;">170ml</div>
  </section>

  <!-- Cajeput wide label -->
  <section class="label wide" style="left:658px;top:342px;">
    <div class="line maker" style="top:36px;">KIEU PHONG DAT</div>
    <div class="line brand" style="top:54px;font-size:22px;">Quirandol</div>
    <div class="ornament" role="img" aria-label="Ornamental scroll band" style="top:148px;width:150px;height:34px;"></div>
    <div class="line variant" style="top:114px;font-size:32px;">Cajeput &nbsp;Oil</div>
    <div class="line fine" style="top:182px;">100% pure oil, 100% organic, 100% environment and human friendly</div>
    <div class="line fine" style="top:192px;">10ml</div>
  </section>

  <!-- Company wordmark -->
  <div class="wordmark">
    <span class="wordmark-dot"></span>
    <span class="wordmark-name">KIEU PHONG DAT</span>
  </div>

</main>
</body>
</html>
```